Business card design for new, innovative company - BluePlinth

We are a new company looking for a business card design that is fun, different and quirky. Must use corporate colour green - CMYK C:55, M:0, Y:100, K:0, and corporate colour grey - C:0, M:0, Y: 0, K:70.

We have developed the first real time data application, in which people are able to profile the data of their existing customers in order to pull out more good fit clients to direct their marketing activities at.

Industry/Entity Type

Marketing

Requirements
Must have
• Logo, name, title, telephone number, fax number, email, website, address

```html
<!DOCTYPE html>
<html lang="en">
<head>
<meta charset="utf-8">
<title>BluePlinth Business Card</title>
<link rel="stylesheet" href="https://fonts.googleapis.com/css2?family=Montserrat:wght@500;600;800&family=Roboto+Slab:wght@700&display=swap">
<style>
  :root {
    --brand-green: #7cc242;
    --brand-grey: #6d6e71;
    --panel-grey: #58595b;
    --deep-grey: #414244;
    --card-white: #f7f7f7;
    --stage: #e9eaeb;
    --ink-light: #ffffff;
  }
  * { margin: 0; padding: 0; box-sizing: border-box; }
  html, body {
    width: 1200px; height: 692px; overflow: hidden;
    background: var(--stage);
    font-family: "Montserrat", Arial, sans-serif;
  }
  .sheet {
    position: relative; width: 1200px; height: 692px;
    display: flex; align-items: center; justify-content: center; gap: 40px;
  }
  .card {
    position: relative; width: 540px; height: 309px;
    background: var(--card-white);
    overflow: hidden;
    box-shadow: 0 6px 18px rgba(0,0,0,0.18);
  }
  .card-shapes { position: absolute; inset: 0; width: 100%; height: 100%; }
  .brand-name {
    position: absolute; display: flex; align-items: center; gap: 10px;
    font-weight: 800; color: var(--brand-green); letter-spacing: -0.5px;
    white-space: nowrap;
  }
  .brand-square { display: block; background: var(--brand-grey); }

  /* Front */
  .front .website {
    position: absolute; left: 282px; top: 34px;
    font-family: "Roboto Slab", Georgia, serif; font-weight: 700;
    font-size: 13px; color: var(--deep-grey);
  }
  .front .brand-name { left: 238px; top: 52px; font-size: 40px; }
  .front .brand-square { width: 22px; height: 22px; }

  /* Back */
  .back .brand-name { left: 24px; top: 22px; font-size: 26px; }
  .back .brand-square { width: 16px; height: 16px; }
  .person-name {
    position: absolute; right: 30px; top: 56px;
    font-size: 21px; font-weight: 500; color: var(--ink-light);
    white-space: nowrap;
  }
  .contact-list {
    position: absolute; right: 24px; top: 130px;
    list-style: none; text-align: right;
  }
  .contact-list li {
    display: flex; justify-content: flex-end; align-items: center; gap: 10px;
    height: 26px; font-size: 13px; font-weight: 500; color: var(--ink-light);
    white-space: nowrap;
  }
  .contact-icon { width: 16px; height: 16px; flex: none; }
  .address {
    position: absolute; left: 0; right: 0; top: 258px; text-align: center;
    font-family: "Roboto Slab", Georgia, serif; font-weight: 700;
    font-size: 13px; color: var(--brand-green);
  }
</style>
</head>
<body>
<main class="sheet">

  <section class="card front" aria-label="Business card front">
    <svg class="card-shapes" viewBox="0 0 540 309" aria-hidden="true">
      <path d="M0 309 L0 292 C140 262 250 175 540 118 L540 309 Z" fill="var(--panel-grey)"/>
      <path d="M210 214 C300 164 420 128 540 106" fill="none" stroke="var(--brand-green)" stroke-width="5"/>
    </svg>
    <p class="website">www.blueplinth.com</p>
    <h1 class="brand-name"><span class="brand-square"></span>BluePlinth</h1>
  </section>

  <section class="card back" aria-label="Business card back">
    <svg class="card-shapes" viewBox="0 0 540 309" aria-hidden="true">
      <path d="M540 8 L300 22 C255 26 235 80 205 150 C175 220 125 246 40 250 L540 250 Z" fill="var(--panel-grey)"/>
      <path d="M150 200 C195 120 220 70 240 40 C255 18 280 12 310 10 L540 0" fill="none" stroke="var(--brand-green)" stroke-width="4"/>
      <rect x="0" y="284" width="540" height="25" fill="var(--panel-grey)"/>
    </svg>
    <h2 class="brand-name"><span class="brand-square"></span>BluePlinth</h2>
    <p class="person-name">Clara Whitfield</p>
    <ul class="contact-list">
      <li>07700900123
        <svg class="contact-icon" viewBox="0 0 16 16" aria-hidden="true"><rect x="4" y="1" width="8" height="14" rx="1.5" fill="none" stroke="var(--brand-green)" stroke-width="1.6"/><rect x="6" y="3.5" width="4" height="4" fill="var(--brand-green)"/></svg>
      </li>
      <li>01632 960457
        <svg class="contact-icon" viewBox="0 0 16 16" aria-hidden="true"><path d="M3 1.5 L6 1.5 L7 5 L5 6.5 C6 8.8 7.2 10 9.5 11 L11 9 L14.5 10 L14.5 13 C14.5 14 13.5 14.8 12.5 14.6 C7 13.8 2.2 9 1.4 3.5 C1.2 2.5 2 1.5 3 1.5 Z" fill="var(--brand-green)"/></svg>
      </li>
      <li>clara.whitfield@northgatesupply.com
        <svg class="contact-icon" viewBox="0 0 16 16" aria-hidden="true"><rect x="1" y="3" width="14" height="10" fill="var(--brand-green)"/><path d="M1 3 L8 9 L15 3" fill="none" stroke="var(--panel-grey)" stroke-width="1.3"/></svg>
      </li>
    </ul>
    <p class="address">22a Fenwick Road, Ely, Cambridgeshire, CB7 4ZZ</p>
  </section>

</main>
</body>
</html>
```